New Business Card for General Contractor Marketing

Need a business card the is more like a marketing promotion of our services
Must be horizontal orientation, One Sided Only, Max font size, Organize the Services
#1 General Contractor for Realtors
Remodels – Renovations – Repairs
Water & Mold Damage Experts
Painting: Interior/ Exterior
Flooring: Wood / LVT / Carpet
Plumbing: Repairs & Upgrades
Electric: Lights & Energy Efficient Upgrades
Kitchen & Bath Remodels
Fast Inspections Repair Billed Thru Escrow
BrightHarborBuilds.com
555-418-2796

Industry/Entity Type

General Contractor

Contact Information for Business Card

One Sided Only: #1 General Contractor for Realtors Remodels – Renovations – Repairs Water & Mold Damage Experts Painting: Interior/ Exterior Flooring: Wood / LVT / Carpet Plumbing: Repairs & Upgrades Electric: Lights & Energy Efficient Upgrades Kitchen & Bath Remodels Fast Inspections Repair Billed Thru Escrow BrightHarborBuilds.com 555-418-2796

Colors
0054AA
0677BA
7BADD7
CADEEF
E8F1F8

Requirements
Must have
• One Sided Only: #1 General Contractor for Realtors Remodels – Renovations – Repairs Water & Mold Damage Experts Painting: Interior/ Exterior Flooring: Wood / LVT / Carpet Plumbing: Repairs & Upgrades Electric: Lights & Energy Efficient Upgrades Kitchen & Bath Remodels Fast Inspections Repair Billed Thru Escrow BrightHarborBuilds.com 555-418-2796

```html
<!DOCTYPE html>
<html lang="en">
<head>
<meta charset="utf-8">
<title>Bright Harbor Builds – Business Card</title>
<link rel="stylesheet" href="https://fonts.googleapis.com/css2?family=Didact+Gothic&family=Montserrat:wght@700;800&display=swap">
<style>
  :root {
    --backdrop: #c5c9d3;
    --card: #ffffff;
    --navy: #1a2a55;
    --orange: #ff7f00;
    --list-text: #f2f2f2;
  }
  html, body {
    margin: 0;
    width: 1200px;
    height: 1200px;
    overflow: hidden;
    background: var(--backdrop);
  }
  .card {
    position: absolute;
    left: 50px;
    top: 286px;
    width: 1100px;
    height: 629px;
    background: var(--card);
    border-radius: 78px;
    overflow: hidden;
  }
  .card__panel {
    position: absolute;
    inset: 0;
    width: 100%;
    height: 100%;
  }
  .services {
    position: absolute;
    left: 94px;
    top: 158px;
    margin: 0;
    padding: 0;
    list-style: none;
    font-family: "Didact Gothic", sans-serif;
    font-size: 24px;
    line-height: 35.5px;
    color: var(--list-text);
  }
  .services li {
    position: relative;
    padding-left: 20px;
    white-space: nowrap;
  }
  .services li::before {
    content: "";
    position: absolute;
    left: 0;
    top: 13px;
    width: 9px;
    height: 9px;
    border-radius: 50%;
    background: var(--orange);
  }
  .contact {
    position: absolute;
    left: 760px;
    width: 300px;
    top: 295px;
    text-align: center;
    font-family: "Montserrat", sans-serif;
    font-weight: 700;
  }
  .contact__name {
    margin: 0 0 18px;
    font-size: 19px;
    color: var(--navy);
    text-transform: uppercase;
    letter-spacing: 0.2px;
  }
  .contact__web {
    margin: 0;
    font-size: 19px;
    color: var(--orange);
  }
  .contact__phone {
    margin: 4px 0 0;
    font-size: 27px;
    color: var(--orange);
  }
</style>
</head>
<body>
  <main class="card">
    <svg class="card__panel" viewBox="0 0 1462 836" preserveAspectRatio="none" aria-hidden="true">
      <path fill="var(--orange)" d="M0 0 H255 C700 30 968 200 968 418 C968 636 700 806 255 836 H0 Z"/>
      <path fill="var(--navy)" d="M0 0 H255 C680 30 943 200 943 418 C943 636 680 806 255 836 H0 Z"/>
    </svg>

    <ul class="services">
      <li>#1 General Contractor for Realtors</li>
      <li>Remodels – Renovations – Repairs</li>
      <li>Water &amp; Mold Damage Experts</li>
      <li>Painting: Interior/ Exterior</li>
      <li>Flooring: Wood / LVT / Carpet</li>
      <li>Plumbing: Repairs &amp; Upgrades</li>
      <li>Electric: Lights &amp; Energy Efficient Upgrades</li>
      <li>Kitchen &amp; Bath Remodels</li>
      <li>Fast Inspections Repair Billed Thru Escrow</li>
    </ul>

    <section class="contact">
      <p class="contact__name">Bright Harbor Builds</p>
      <p class="contact__web">brightharborbuilds.com</p>
      <p class="contact__phone">555-418-2796</p>
    </section>
  </main>
</body>
</html>
```